Brindale transport business cards

Front of card, Looking for my logo on one side of the card

Back of card,
Brindale Transport Maintenance
Onsite Cars, Trucks & trailer maintenance and repairs
Ronan Brindale
0452819036
Brindaletm@fernmail.com

```html
<!DOCTYPE html>
<html lang="en">
<head>
<meta charset="utf-8">
<title>Brindale Transport Maintenance – Business Cards</title>
<link rel="stylesheet" href="https://fonts.googleapis.com/css2?family=Montserrat:wght@500;800&family=Oswald:wght@500&display=swap">
<style>
  :root {
    --backdrop: #3a3a3c;
    --card-white: #ffffff;
    --card-black: #1c1c1c;
    --brand-blue: #1a6fc9;
    --ink: #141414;
    --paper: #ffffff;
  }
  * { box-sizing: border-box; margin: 0; padding: 0; }
  html, body { width: 1200px; height: 1200px; overflow: hidden; }
  body { background: var(--backdrop); position: relative; font-family: "Montserrat", sans-serif; }

  .card {
    position: absolute;
    width: 720px;
    height: 412px;
    border-radius: 34px;
    overflow: hidden;
    box-shadow: 0 18px 40px rgba(0,0,0,0.45);
  }

  /* Contact side */
  .card--contact { left: 120px; top: 110px; background: var(--card-white); }
  .card__bands { position: absolute; inset: 0; }

  .wordmark { position: absolute; display: flex; align-items: center; gap: 14px; }
  .wordmark__dot { width: 22px; height: 22px; border-radius: 50%; background: var(--brand-blue); flex: none; }
  .wordmark__name { font-weight: 800; text-transform: uppercase; line-height: 1.05; }
  .card--contact .wordmark { left: 180px; top: 58px; }
  .card--contact .wordmark__name { color: var(--ink); font-size: 30px; }

  .tagline {
    position: absolute; left: 150px; top: 178px;
    font-family: "Oswald", sans-serif; font-weight: 500;
    font-size: 23px; letter-spacing: 0.2px; text-transform: uppercase;
    color: var(--brand-blue);
  }
  .rule { position: absolute; height: 2px; background: var(--brand-blue); }
  .rule--top { left: 150px; top: 224px; width: 520px; }
  .rule--mid { left: 150px; top: 330px; width: 300px; height: 1.5px; }

  .person { position: absolute; left: 150px; top: 242px; }
  .person__name { font-weight: 500; font-size: 34px; color: var(--brand-blue); text-transform: uppercase; line-height: 1; }
  .person__role { font-weight: 500; font-size: 18px; color: var(--ink); text-transform: uppercase; margin-top: 4px; }

  .contacts { position: absolute; left: 150px; top: 340px; list-style: none; }
  .contacts li { display: flex; align-items: center; gap: 12px; font-size: 17px; color: var(--ink); height: 26px; }
  .contacts svg { width: 20px; height: 20px; fill: var(--brand-blue); flex: none; }

  /* Logo side */
  .card--logo { left: 360px; top: 660px; background: var(--card-black); }
  .card--logo .wordmark { left: 0; right: 0; top: 0; bottom: 0; justify-content: center; }
  .card--logo .wordmark__name { color: var(--paper); font-size: 44px; }
</style>
</head>
<body>

  <section class="card card--contact" aria-label="Business card contact side">
    <svg class="card__bands" viewBox="0 0 720 412" preserveAspectRatio="none" aria-hidden="true">
      <polygon points="0,392 450,392 450,318 470,318 470,412 0,412" fill="var(--brand-blue)"/>
      <polygon points="480,306 720,306 720,412 480,412" fill="var(--ink)"/>
    </svg>

    <div class="wordmark">
      <span class="wordmark__dot"></span>
      <span class="wordmark__name">Brindale<br>Transport Maintenance</span>
    </div>

    <p class="tagline">Onsite cars, trucks &amp; trailer maintenance and repairs</p>
    <div class="rule rule--top"></div>

    <div class="person">
      <p class="person__name">Ronan Brindale</p>
      <p class="person__role">Owner</p>
    </div>
    <div class="rule rule--mid"></div>

    <ul class="contacts">
      <li>
        <svg viewBox="0 0 24 24" aria-hidden="true"><path d="M6.6 10.8a15.1 15.1 0 0 0 6.6 6.6l2.2-2.2a1 1 0 0 1 1-.25 11.4 11.4 0 0 0 3.6.57 1 1 0 0 1 1 1V20a1 1 0 0 1-1 1A17 17 0 0 1 3 4a1 1 0 0 1 1-1h3.5a1 1 0 0 1 1 1c0 1.25.2 2.45.57 3.57a1 1 0 0 1-.25 1z"/></svg>
        0452819036
      </li>
      <li>
        <svg viewBox="0 0 24 24" aria-hidden="true"><path d="M2 5h20v14H2zm2 2v.4l8 5.2 8-5.2V7zm0 2.8V17h16V9.8l-8 5.2z"/></svg>
        Brindaletm@fernmail.com
      </li>
    </ul>
  </section>

  <section class="card card--logo" aria-label="Business card logo side">
    <div class="wordmark">
      <span class="wordmark__dot"></span>
      <span class="wordmark__name">Brindale<br>Transport Maintenance</span>
    </div>
  </section>

</body>
</html>
```